Modern business card design "MAPLE NINE"

Please design modern business card for MAPLE NINE.
Must be black or dark gray back ground front side and back side with white letter.

Infomation

CEO PRESIDENT
OWEN DARBY
WWW.MAPLE9.EXAMPLE

+1 555 014 2297
INFO@MAPLE9.EXAMPLE
48 LINDEN CT PALM VALE, CA 90001

```html
<!DOCTYPE html>
<html lang="en">
<head>
<meta charset="utf-8">
<title>MAPLE NINE Business Card</title>
<link rel="stylesheet" href="https://fonts.googleapis.com/css2?family=Montserrat:wght@300;400;700&display=swap">
<style>
  :root {
    --page: #3a3a3c;
    --card: #1f1d21;
    --ink: #ffffff;
    --ink-soft: rgba(255,255,255,0.55);
  }
  * { margin: 0; padding: 0; box-sizing: border-box; }
  html, body { width: 1200px; height: 900px; overflow: hidden; }
  body {
    background: var(--page);
    font-family: "Montserrat", Arial, sans-serif;
    color: var(--ink);
    display: flex;
    flex-direction: column;
    align-items: center;
    justify-content: center;
    gap: 48px;
  }
  .card {
    width: 700px;
    height: 400px;
    background: var(--card);
    position: relative;
    box-shadow: 0 6px 20px rgba(0,0,0,0.35);
  }
  /* Front side */
  .card-front {
    display: flex;
    flex-direction: column;
    align-items: center;
    justify-content: center;
  }
  .brand {
    display: flex;
    align-items: center;
    gap: 22px;
    font-weight: 300;
    font-size: 46px;
    letter-spacing: 6px;
  }
  .brand-mark {
    width: 40px;
    height: 40px;
    border: 3px solid var(--ink);
  }
  .web-rule {
    display: flex;
    align-items: center;
    gap: 14px;
    margin-top: 34px;
    width: 560px;
  }
  .web-rule .line { flex: 1; height: 1px; background: var(--ink-soft); }
  .web-rule .url { font-size: 14px; letter-spacing: 1px; }

  /* Back side */
  .card-back {
    display: flex;
    align-items: center;
    padding: 0 60px;
  }
  .contact { flex: 1; }
  .contact .title { font-size: 15px; letter-spacing: 1px; }
  .contact .name { font-size: 26px; font-weight: 700; letter-spacing: 2px; margin-top: 6px; }
  .contact .details { margin-top: 22px; font-size: 15px; line-height: 1.8; letter-spacing: 0.5px; }
  .socials { display: flex; gap: 12px; margin-top: 20px; }
  .socials span {
    width: 24px; height: 24px; border-radius: 50%;
    background: var(--ink);
  }
  .back-mark {
    display: flex;
    flex-direction: column;
    align-items: center;
    gap: 18px;
  }
  .back-mark .square {
    width: 150px;
    height: 150px;
    border: 14px solid var(--ink);
  }
  .back-mark .label { font-weight: 300; font-size: 20px; letter-spacing: 4px; }
</style>
</head>
<body>
  <section class="card card-front">
    <div class="brand">
      <span>MAPLE</span>
      <span class="brand-mark"></span>
      <span>NINE</span>
    </div>
    <div class="web-rule">
      <span class="line"></span>
      <span class="url">WWW.MAPLE9.EXAMPLE</span>
      <span class="line"></span>
    </div>
  </section>

  <section class="card card-back">
    <div class="contact">
      <p class="title">CEO PRESIDENT</p>
      <p class="name">OWEN DARBY</p>
      <div class="details">
        <p>+1 555 014 2297</p>
        <p>INFO@MAPLE9.EXAMPLE</p>
        <p>WWW.MAPLE9.EXAMPLE</p>
        <p>48 LINDEN CT PALM VALE, CA 90001</p>
      </div>
      <div class="socials" aria-label="Social profiles">
        <span></span><span></span><span></span><span></span><span></span>
      </div>
    </div>
    <div class="back-mark">
      <span class="square"></span>
      <span class="label">MAPLE NINE</span>
    </div>
  </section>
</body>
</html>
```